Kickass billboard for motorway

We take dented trucks - clue is in the name.
We have a 45ft billboard we're looking to design constructed from an old trailer we own (so we can be as creative as possible).
We provide a van buying service, being one of the only companies in the UK with the facilities to recover faulty, damaged and broken vans - from small car derived vans to large trucks and lorries.
ur niche in the market is different to car buying services, as buying and selling cars is often an emotionally driven process, whereas people often see and treat vans purely as a tool. There are alternatives to a car, public transport etc, but not to a work van - so people go out straight away and replace them immediately, often leaving the old broken van to sit on their drive or in their unit.
Looking to start building a brand asset bank.
Feel free to check out our website to get a feel for what we do:
Wetakedentedtrucks.co.uk

Target Market(s)

Van owners/drivers & fleet managers

Industry/Entity Type

Automotive

Font styles to use
Sans Serif

Colors
34a7d8

Requirements
Must have
• Eye-catching - very eye-catching.
We want to advertise the fact we collect vehicles for free.
We pay instantly upon arrival.
Our phone number 0161 473 2046
Our website www.wetakedentedtrucks.co.uk
Nice to have
• 3d elements - we have the ability to get 3d props for the billboard including damaged vans etc.

```html
<!DOCTYPE html>
<html lang="en">
<head>
<meta charset="utf-8">
<title>Motorway Billboard – Design Options</title>
<link rel="stylesheet" href="https://fonts.googleapis.com/css2?family=Jost:wght@400;500;600&family=Andika&display=swap">
<style>
  :root {
    --board-bg: #545454;
    --brand-blue: #34a7d8;
    --white: #ffffff;
    --rule-cyan: #2fe2f2;
    --rule-amber: #f3b21c;
    --label-grey: #d2d2d2;
    --note-grey: #e2e2e2;
    --cash-light: #ece8ee;
    --cash-purple: #9a8fc4;
    --skin: #e1b08f;
    --van-white: #f1f1f1;
    --van-grey: #b8b8b8;
    --tow-red: #5a2430;
  }
  * { box-sizing: border-box; margin: 0; padding: 0; }
  html, body { width: 1200px; height: 675px; overflow: hidden; }
  body {
    position: relative;
    background: var(--board-bg);
    font-family: "Jost", sans-serif;
    color: var(--white);
  }

  .billboard {
    position: absolute;
    left: 77px;
    width: 675px;
    height: 231px;
    background: var(--brand-blue);
    overflow: hidden;
  }
  .billboard--stacked { top: 73px; }
  .billboard--banner  { top: 371px; }

  .photo { position: absolute; }
  .photo--cash {
    background:
      radial-gradient(ellipse 45% 30% at 35% 85%, var(--skin) 0 60%, transparent 62%),
      linear-gradient(150deg, var(--cash-light) 0%, var(--cash-purple) 55%, var(--cash-light) 100%);
    border-radius: 40% 40% 0 0 / 30% 30% 0 0;
  }
  .photo--tow {
    background:
      linear-gradient(90deg, var(--van-white) 0 58%, var(--tow-red) 64% 100%);
    border-radius: 3px;
    box-shadow: inset 0 -10px 0 var(--van-grey);
  }

  .headline { position: absolute; font-weight: 600; line-height: 1; white-space: nowrap; }
  .billboard--stacked .headline { left: 161px; top: 101px; font-size: 34px; line-height: 40px; }
  .billboard--banner .headline { left: 39px; top: 18px; font-size: 37px; }

  .promise { position: absolute; font-weight: 400; letter-spacing: 0.04em; }
  .billboard--stacked .promise { left: 478px; top: 49px; font-size: 15px; line-height: 19px; }
  .billboard--banner .promise { left: 219px; top: 106px; font-size: 17.5px; line-height: 22px; }

  .rule { position: absolute; left: 0; right: 0; top: 184px; height: 3px; }
  .rule--cyan { background: var(--rule-cyan); }
  .rule--amber { background: var(--rule-amber); }

  .contact { position: absolute; top: 200px; font-weight: 400; font-size: 17px; letter-spacing: 0.02em; white-space: nowrap; }
  .billboard--stacked .contact--web { left: 124px; }
  .billboard--stacked .contact--phone { left: 402px; }
  .billboard--banner .contact { font-size: 17.5px; }
  .billboard--banner .contact--web { left: 139px; }
  .billboard--banner .contact--phone { left: 466px; }

  .option-label {
    position: absolute;
    left: 112px;
    font-family: "Andika", sans-serif;
    font-size: 21px;
    color: var(--label-grey);
  }
  .option-label--one { top: 323px; }
  .option-label--two { top: 620px; }

  .designer-note {
    position: absolute;
    left: 798px;
    top: 283px;
    width: 380px;
    font-family: "Andika", sans-serif;
    font-size: 20.5px;
    line-height: 28.6px;
    letter-spacing: 0.03em;
    color: var(--note-grey);
  }
</style>
</head>
<body>

  <section class="billboard billboard--stacked">
    <div class="photo photo--cash" style="left:20px; top:27px; width:147px; height:204px;" role="img" aria-label="Hand holding a fan of twenty pound notes"></div>
    <h1 class="headline">Get rid of it in<br>less than 24 hours!</h1>
    <p class="promise">Free valuation<br>Instant Payment</p>
    <div class="photo photo--tow" style="left:477px; top:111px; width:174px; height:74px;" role="img" aria-label="Box van being towed by a recovery truck"></div>
    <div class="rule rule--cyan"></div>
    <p class="contact contact--web">www.wetakedentedtrucks.co.uk</p>
    <p class="contact contact--phone">0161 473 2046</p>
  </section>
  <p class="option-label option-label--one">Design 1</p>

  <section class="billboard billboard--banner">
    <h2 class="headline">Get rid of it in less than 24 hours!</h2>
    <div class="photo photo--cash" style="left:20px; top:74px; width:144px; height:157px;" role="img" aria-label="Hand holding a fan of twenty pound notes"></div>
    <p class="promise">Free valuation<br>Instant Paying</p>
    <div class="photo photo--tow" style="left:386px; top:76px; width:262px; height:109px;" role="img" aria-label="Box van being towed by a recovery truck"></div>
    <div class="rule rule--amber"></div>
    <p class="contact contact--web">www.wetakedentedtrucks.co.uk</p>
    <p class="contact contact--phone">0161 473 2046</p>
  </section>
  <p class="option-label option-label--two">Design 2</p>

  <p class="designer-note">*The car being towed can be a stock photo or a combination of a real photo of the existing car and parts of the car.</p>

</body>
</html>
```